Business Card Design Project

I require a business card with the following information on them for various different people;
name
m:
f:
e:
I have a logo already and will attached that. We are in the construction industry. I require something clean and simple but eye catching at the same time. You can use another colour with our logo if you like and you can style the logo as well if you wish. I am open.
Also it needs to be front and back design.
Industry/Entity Type
Construction
Requirements
Must have
- Logo, name, mobile, fax and email address.
Front and back design

```html
<!DOCTYPE html>
<html lang="en">
<head>
<meta charset="utf-8">
<title>Fairbank Developments – Business Card</title>
<link href="https://fonts.googleapis.com/css2?family=Questrial&family=Arimo:wght@400&display=swap" rel="stylesheet">
<style>
  :root {
    --brand-green: #5aad28;
    --brand-green-dark: #3f9a1e;
    --brand-green-light: #9ad24a;
    --tab-grey: #e4e4e4;
    --card-white: #ffffff;
    --card-border: #b9b9b9;
    --ink: #111111;
    --page: #ffffff;
  }
  * { box-sizing: border-box; margin: 0; padding: 0; }
  html, body {
    width: 1200px; height: 900px; overflow: hidden;
    background: var(--page);
  }
  .canvas { position: relative; width: 1200px; height: 900px; }

  .card {
    position: absolute; top: 282px; width: 523px; height: 298px;
    border-radius: 14px;
    box-shadow: 3px 4px 6px rgba(0,0,0,0.28);
    overflow: hidden;
  }
  .card--front { left: 60px; background: var(--card-white); border: 1px solid var(--card-border); }
  .card--back { left: 628px; background: var(--brand-green); }

  .side-tab {
    position: absolute; top: 51px; width: 14px; height: 195px;
  }
  .card--front .side-tab {
    background: linear-gradient(90deg, var(--brand-green-dark), var(--brand-green-light) 60%, var(--brand-green));
  }
  .card--back .side-tab { background: var(--tab-grey); }
  .side-tab--left { left: 0; border-radius: 0 6px 6px 0; }
  .side-tab--right { right: 0; border-radius: 6px 0 0 6px; }
  .card--front .side-tab--left { left: -1px; }
  .card--front .side-tab--right { right: -1px; }

  .wordmark {
    position: absolute; display: flex; align-items: center; gap: 16px;
    font-family: "Questrial", sans-serif; font-weight: 400;
  }
  .wordmark__square { width: 46px; height: 46px; border-radius: 4px; flex: none; }
  .wordmark__name { font-size: 30px; line-height: 1; letter-spacing: 0.3px; white-space: nowrap; }

  .card--front .wordmark { left: 60px; top: 114px; }
  .card--front .wordmark__square { background: var(--brand-green); }
  .card--front .wordmark__name { color: var(--brand-green); }

  .card--back .wordmark { right: 58px; top: 120px; flex-direction: row-reverse; }
  .card--back .wordmark__square { background: #ffffff; }
  .card--back .wordmark__name { color: #ffffff; }

  .contact {
    position: absolute; left: 76px; top: 212px;
    font-family: "Arimo", sans-serif; color: var(--ink);
  }
  .contact__name { font-size: 23px; line-height: 28px; }
  .contact__line { font-size: 17px; line-height: 22px; padding-left: 10px; white-space: pre; }
</style>
</head>
<body>
<main class="canvas">
  <section class="card card--front" aria-label="Business card front">
    <span class="side-tab side-tab--left"></span>
    <span class="side-tab side-tab--right"></span>
    <div class="wordmark">
      <span class="wordmark__square"></span>
      <span class="wordmark__name">Fairbank Developments</span>
    </div>
    <div class="contact">
      <p class="contact__name">name xxxxxxx.......</p>
      <p class="contact__line">m : xxxxxxxxxxxx  f : xxxxxxxxxxxx</p>
      <p class="contact__line">e  : xxxxxxx@xxxx.com</p>
    </div>
  </section>

  <section class="card card--back" aria-label="Business card back">
    <span class="side-tab side-tab--left"></span>
    <span class="side-tab side-tab--right"></span>
    <div class="wordmark">
      <span class="wordmark__square"></span>
      <span class="wordmark__name">Fairbank Developments</span>
    </div>
  </section>
</main>
</body>
</html>
```